I need a logo design and a business card design for a new strategy consultancy that I set up called Tessaron LLC. We help clients make strategically important decisions, cutting through the cloud of noise. The design should imply clarity, simplicity and wisdom.

```html
<!DOCTYPE html>
<html lang="en">
<head>
<meta charset="utf-8">
<title>Tessaron LLC — Business Card</title>
<link rel="stylesheet" href="https://fonts.googleapis.com/css2?family=Cinzel:wght@600;700&family=Tinos&display=swap">
<style>
  :root {
    --backdrop: #e4e0da;
    --card-white: #fbfbfb;
    --card-shade: #efefef;
    --brand-purple: #7670b4;
    --brand-red: #e2262b;
    --ink: #3e3e3e;
    --rule: #3a3a3a;
    --faint-grey: #e2e2e2;
    --faint-light: rgba(255, 255, 255, 0.1);
    --white: #ffffff;
  }
  html, body {
    margin: 0;
    padding: 0;
    width: 900px;
    height: 1200px;
    overflow: hidden;
    background: var(--backdrop);
  }
  .canvas {
    position: relative;
    width: 900px;
    height: 1200px;
  }
  .card {
    position: absolute;
    overflow: hidden;
    box-shadow: 0 3px 10px rgba(0, 0, 0, 0.35);
  }
  .card--front {
    left: 78px; top: 145px; width: 735px; height: 428px;
    background: radial-gradient(ellipse at 25% 60%, var(--card-white) 0%, var(--card-white) 45%, var(--card-shade) 100%);
  }
  .card--back {
    left: 78px; top: 628px; width: 740px; height: 432px;
    background: var(--brand-purple);
  }
  .decor-circle {
    position: absolute;
    border-radius: 50%;
  }
  .card--front .decor-circle {
    left: 420px; top: 20px; width: 300px; height: 300px;
    background: var(--faint-grey);
  }
  .card--back .decor-circle {
    left: 390px; top: 10px; width: 400px; height: 400px;
    background: var(--faint-light);
  }
  .brand {
    position: absolute;
    display: flex;
    align-items: center;
    gap: 22px;
  }
  .brand__mark {
    width: 62px; height: 62px;
    border-radius: 50%;
  }
  .brand__name {
    font-family: "Cinzel", serif;
    font-weight: 600;
    font-size: 44px;
    letter-spacing: 1px;
    line-height: 1;
    white-space: nowrap;
  }
  .card--front .brand { left: 38px; top: 82px; }
  .card--front .brand__mark { background: var(--brand-purple); }
  .card--front .brand__name { color: var(--brand-purple); }
  .card--back .brand { left: 152px; top: 180px; }
  .card--back .brand__mark { background: var(--white); }
  .card--back .brand__name { color: var(--white); }
  .person {
    position: absolute;
    left: 37px; top: 274px;
    font-family: "Cinzel", serif;
  }
  .person__name {
    margin: 0;
    font-weight: 700;
    font-size: 21px;
    letter-spacing: 0.5px;
    color: var(--ink);
  }
  .person__role {
    margin: 2px 0 0;
    font-weight: 600;
    font-size: 17px;
    letter-spacing: 0.5px;
    color: var(--brand-red);
  }
  .divider {
    position: absolute;
    left: 37px; top: 331px;
    width: 654px; height: 1px;
    background: var(--rule);
  }
  .contact {
    position: absolute;
    left: 37px; top: 342px;
    margin: 0; padding: 0;
    list-style: none;
    font-family: "Tinos", serif;
    font-size: 15.5px;
    color: var(--ink);
  }
  .contact__item {
    display: flex;
    align-items: center;
    gap: 12px;
    height: 24px;
  }
  .contact__icon { width: 14px; height: 14px; fill: var(--brand-red); }
  .address {
    position: absolute;
    right: 44px; top: 342px;
    font-family: "Tinos", serif;
    font-size: 15.5px;
    line-height: 24px;
    color: var(--ink);
    text-align: right;
    font-style: normal;
  }
</style>
</head>
<body>
<main class="canvas">
  <section class="card card--front" aria-label="Business card front">
    <div class="decor-circle" aria-hidden="true"></div>
    <div class="brand">
      <span class="brand__mark" aria-hidden="true"></span>
      <span class="brand__name">TESSARON LLC</span>
    </div>
    <div class="person">
      <h1 class="person__name">MARCUS WHITFIELD</h1>
      <p class="person__role">CEO/FOUNDER</p>
    </div>
    <div class="divider" aria-hidden="true"></div>
    <ul class="contact">
      <li class="contact__item">
        <svg class="contact__icon" viewBox="0 0 24 24" aria-hidden="true"><path d="M6.6 10.8a15 15 0 0 0 6.6 6.6l2.2-2.2a1 1 0 0 1 1-.25 11.4 11.4 0 0 0 3.6.57 1 1 0 0 1 1 1V20a1 1 0 0 1-1 1A17 17 0 0 1 3 4a1 1 0 0 1 1-1h3.5a1 1 0 0 1 1 1c0 1.25.2 2.45.57 3.57a1 1 0 0 1-.25 1z"/></svg>
        <span>230.555.0147</span>
      </li>
      <li class="contact__item">
        <svg class="contact__icon" viewBox="0 0 24 24" aria-hidden="true"><path d="M2 5h20v14H2z M2 5l10 8 10-8" stroke="#fff" stroke-width="1.5"/></svg>
        <span>marcus@tessaron.com</span>
      </li>
    </ul>
    <address class="address">842 W. Harbor Lane<br>Suite B, Corvell, CA 92614</address>
  </section>

  <section class="card card--back" aria-label="Business card back">
    <div class="decor-circle" aria-hidden="true"></div>
    <div class="brand">
      <span class="brand__mark" aria-hidden="true"></span>
      <span class="brand__name">TESSARON LLC</span>
    </div>
  </section>
</main>
</body>
</html>
```